Still Harbor Weekend book cover design

I have attached an image that I would like this front cover to be similar to. This is a book about marriage so there will need to be a man and woman on the front cover and I am open to your creative design from that point. I have also attached the ISBN barcode and photo of authors for back cover. Book details are below:

Title:
Still HARBOR WEEKEND
Tending Covenant
A Workbook for the Shared Home and Kin

Authors: LEON AND TASHA’ MORVILLE
Book size : 8x10
Back cover text:
LEON AND TASHA’ MORVILLE

Authors, parents, grandparents, business owners, and public speakers, has served in ministry for over 25 years. They are the founders of Rise Forth Global Fellowship, serving as the senior pastors. They are also currently serving as national and international mission directors. They both are very intentional about assisting couples in developing their marriages. Having firsthand knowledge of God’s mercy in this area, the Morvilles are sharing the power of tending covenant with dedication and simplicity.

They are blessed to have three married children, and thirteen grandchildren in their more than 40 years of marriage. They are currently residing in Birmingham, Alabama. They look forward seeing you soon.

Back cover photo: Attached

```html
<!DOCTYPE html>
<html lang="en">
<head>
<meta charset="utf-8">
<title>Still Harbor Weekend — Book Cover</title>
<link href="https://fonts.googleapis.com/css2?family=EB+Garamond:ital,wght@0,400;0,500;1,400&family=Oswald:wght@500&display=swap" rel="stylesheet">
<style>
  :root {
    --paper: #e6d7b4;
    --ink: #3e4f40;
    --art-green: #435544;
    --art-red: #d9432c;
    --art-blush: #e3b3a0;
    --art-rose: #e58fa6;
    --art-line: #2f2f2f;
  }
  html, body {
    margin: 0;
    padding: 0;
    width: 960px;
    height: 1200px;
    overflow: hidden;
    background: var(--paper);
  }
  .cover {
    position: relative;
    width: 960px;
    height: 1200px;
    background: var(--paper);
  }
  .cover-type {
    position: absolute;
    inset: 0;
    width: 960px;
    height: 1200px;
  }
  .title {
    font-family: "EB Garamond", Garamond, serif;
    font-weight: 500;
    font-size: 122px;
    fill: var(--ink);
  }
  .subtitle {
    font-family: "Oswald", "Arial Narrow", sans-serif;
    font-weight: 500;
    font-size: 31px;
    letter-spacing: 4px;
    fill: var(--ink);
  }
  .tagline {
    font-family: "EB Garamond", Garamond, serif;
    font-style: italic;
    font-size: 39px;
    fill: var(--ink);
  }
  .authors {
    font-family: "EB Garamond", Garamond, serif;
    font-weight: 400;
    font-size: 56px;
    fill: var(--ink);
  }
  .couple-art {
    position: absolute;
    left: 236px;
    top: 444px;
    width: 490px;
    height: 488px;
    border-radius: 200px 200px 0 0;
    background:
      radial-gradient(ellipse 40% 30% at 50% 88%, var(--art-rose) 0%, transparent 100%),
      radial-gradient(ellipse 45% 55% at 28% 60%, var(--art-green) 0%, transparent 100%),
      radial-gradient(ellipse 50% 60% at 72% 55%, var(--art-red) 0%, transparent 100%),
      linear-gradient(180deg, var(--art-blush) 0%, var(--art-blush) 100%);
    opacity: 0.92;
  }
  .ground-line {
    stroke: var(--art-line);
    stroke-width: 2;
  }
</style>
</head>
<body>
  <main class="cover">
    <div class="couple-art" role="img" aria-label="Illustration of a man in a red sweater embracing a woman in a green dress, foreheads touching, standing among pink flowers"></div>
    <svg class="cover-type" viewBox="0 0 960 1200" xmlns="http://www.w3.org/2000/svg">
      <text class="title" x="480" y="178" text-anchor="middle" textLength="860" lengthAdjust="spacing">STILL HARBOR</text>
      <text class="title" x="480" y="334" text-anchor="middle">WEEKEND</text>
      <text class="subtitle" x="480" y="415" text-anchor="middle">TENDING COVENANT</text>
      <line class="ground-line" x1="208" y1="933" x2="745" y2="933"/>
      <text class="tagline" x="480" y="1036" text-anchor="middle">A Workbook for the Shared Home and Kin</text>
      <text class="authors" x="480" y="1142" text-anchor="middle">LEON AND TASHA’ MORVILLE</text>
    </svg>
  </main>
</body>
</html>
```